Escape Room Brochure, Trifold. Bold Black, yellow red. Doors Keys

We need a brochure to introduce our escape room and our services.
Attached are some of our designs as well as some examples of brochures we like.
We are THE VAULTS of KDW, however, we are aiming at Can you slip the vaults of KDW.
We are one of three escape rooms in a college town. We believe our rooms are more creative and original. Only family friendly. Brochure to be distributed to explain what an escape room is and promote our new fundraising program.

Font styles to use
Other font styles liked:
• impact

Colors
fbee3e
ec1f27
000000
dbdbdb

Requirements
Must have
• description of our rooms. services we offer. Fundraising and group teambuilding. Most information can be found at thevaultsofkdw.com
• what is an escape room.
Nice to have
• Photoshop
Should not have
• padlock or maze

```html
<!DOCTYPE html>
<html lang="en">
<head>
<meta charset="utf-8">
<title>THE VAULTS of KDW – Brochure Inside Spread</title>
<link href="https://fonts.googleapis.com/css2?family=Anton&family=Open+Sans:wght@400;600&family=Tinos:wght@400;700&display=swap" rel="stylesheet">
<style>
  :root {
    --yellow: #fbee3e;
    --gold: #f5c400;
    --red: #ec1f27;
    --black: #000000;
    --ink: #0b0b0b;
    --grey: #dbdbdb;
    --white: #ffffff;
    --line: #9a9a9a;
  }
  * { margin: 0; padding: 0; box-sizing: border-box; }
  html, body { width: 1200px; height: 847px; overflow: hidden; background: var(--grey); }
  .spread {
    position: relative;
    width: 1200px; height: 847px;
    background: var(--ink);
    overflow: hidden;
    font-family: "Open Sans", Arial, sans-serif;
    color: var(--white);
  }
  .bands, .diagram-lines { position: absolute; inset: 0; }
  .fold { position: absolute; left: 599px; top: 0; width: 2px; height: 847px; background: rgba(255,255,255,0.06); }

  .backdrop {
    position: absolute; left: 300px; top: 330px; width: 620px; height: 330px;
    background: radial-gradient(ellipse at 60% 45%, #2a2724 0%, #15130f 45%, rgba(11,11,11,0) 75%);
  }

  .section-title {
    font-family: "Anton", Impact, sans-serif;
    color: var(--yellow);
    font-size: 34px;
    letter-spacing: 1px;
    line-height: 1;
    text-transform: uppercase;
  }
  .section-copy { font-size: 13px; line-height: 1.42; color: var(--white); }

  .team-building { position: absolute; left: 40px; top: 160px; width: 245px; }
  .team-building .section-copy { margin-top: 10px; text-align: justify; }
  .date-night { position: absolute; left: 850px; top: 80px; width: 320px; }
  .date-night .section-copy { margin-top: 8px; text-align: justify; }

  .photo-strip {
    position: absolute; left: 300px; top: 150px; width: 540px; height: 205px;
    border: 3px solid var(--yellow);
    display: flex;
  }
  .photo { flex: 1; }
  .photo-table { background: linear-gradient(135deg, #5a4a3a, #3b3129 60%, #6b5a48); }
  .photo-group { background: linear-gradient(180deg, #d9c531 0%, #b7a530 45%, #2b2b30 100%); }

  .node {
    position: absolute; width: 84px; height: 84px; border-radius: 50%;
    background: var(--white);
    border: 5px solid var(--grey);
    box-shadow: 0 0 18px rgba(255,255,255,0.45);
    display: flex; align-items: center; justify-content: center;
  }
  .node svg { width: 40px; height: 40px; }
  .node-date { background: var(--yellow); }
  .hub {
    position: absolute; left: 540px; top: 418px; width: 124px; height: 124px; border-radius: 50%;
    background: var(--black); border: 5px solid var(--grey);
    box-shadow: 0 0 22px rgba(255,255,255,0.5);
    display: flex; align-items: center; justify-content: center; text-align: center;
  }
  .hub-name {
    font-family: "Open Sans", Arial, sans-serif; font-weight: 600;
    color: var(--yellow); font-size: 13px; line-height: 1.2;
  }

  .label {
    position: absolute; font-family: "Tinos", "Times New Roman", serif;
    font-weight: 700; font-size: 15px; color: var(--white);
  }
  .label-note {
    position: absolute; font-family: "Tinos", "Times New Roman", serif;
    font-size: 13px; line-height: 1.3; color: var(--white); text-align: right;
  }
</style>
</head>
<body>
<main class="spread">

  <svg class="bands" viewBox="0 0 1200 847" aria-hidden="true">
    <polygon points="470,0 740,0 600,95" fill="var(--red)"/>
    <polygon points="0,118 600,62 1200,0 1200,26 600,96 0,140" fill="var(--gold)"/>
    <polygon points="780,60 1200,0 1200,12 835,90" fill="var(--yellow)"/>
    <polygon points="440,847 760,847 600,745" fill="var(--red)"/>
    <polygon points="0,847 0,830 600,745 610,770 90,847" fill="var(--gold)"/>
    <polygon points="600,745 1200,700 1200,728 620,770" fill="var(--gold)"/>
  </svg>
  <div class="fold"></div>

  <div class="backdrop" role="img" aria-label="Faint photo of an escape room interior"></div>

  <section class="team-building">
    <h2 class="section-title">Team Building</h2>
    <p class="section-copy">Escape games are well-known for being great for team-building. The escape room experience forces everyone in the room to work together, share information, and discuss problems in order to escape in time. They are an amazing option for co-workers looking to boost morale, promote teamwork, or just to create a nice ice-breaker situation that everyone will remember.</p>
  </section>

  <div class="photo-strip">
    <div class="photo photo-table" role="img" aria-label="Photo of hands working on puzzle pieces around a wooden table"></div>
    <div class="photo photo-group" role="img" aria-label="Photo of a group of co-workers posing in a yellow escape room"></div>
  </div>

  <section class="date-night">
    <h2 class="section-title">Date Night</h2>
    <p class="section-copy">If you are a business owner or manager looking to promote a wonderful team environment in your workplace, the escape games at THE VAULTS of KDW are a great option for you that everyone will enjoy. We look forward to seeing you and your team!</p>
  </section>

  <svg class="diagram-lines" viewBox="0 0 1200 847" aria-hidden="true">
    <g stroke="var(--line)" stroke-width="1" fill="none">
      <polyline points="615,395 735,355 860,355"/>
      <polyline points="762,440 840,445 940,445"/>
      <polyline points="760,525 890,555 980,555"/>
      <polyline points="490,463 360,460"/>
      <polyline points="500,556 375,560"/>
      <polyline points="590,640 520,675 440,675"/>
      <line x1="600" y1="480" x2="510" y2="470"/>
      <line x1="600" y1="480" x2="520" y2="550"/>
    </g>
    <g fill="var(--white)">
      <circle cx="860" cy="355" r="2.5"/>
      <circle cx="840" cy="445" r="2.5"/>
      <circle cx="890" cy="555" r="2.5"/>
      <circle cx="360" cy="460" r="2.5"/>
      <circle cx="375" cy="560" r="2.5"/>
      <circle cx="440" cy="675" r="2.5"/>
    </g>
  </svg>

  <div class="node node-team" style="left:575px;top:350px;">
    <svg viewBox="0 0 40 40"><g fill="#000"><circle cx="20" cy="14" r="5"/><circle cx="10" cy="17" r="4"/><circle cx="30" cy="17" r="4"/><path d="M12 32a8 8 0 0 1 16 0z"/><path d="M3 31a7 7 0 0 1 11-5l-2 5z"/><path d="M37 31a7 7 0 0 0-11-5l2 5z"/></g></svg>
  </div>
  <div class="node node-date" style="left:680px;top:400px;">
    <svg viewBox="0 0 40 40"><g fill="#000"><circle cx="9" cy="13" r="4"/><circle cx="31" cy="13" r="4"/><rect x="13" y="20" width="14" height="3"/><rect x="19" y="23" width="2" height="10"/><rect x="6" y="19" width="6" height="8"/><rect x="28" y="19" width="6" height="8"/></g></svg>
  </div>
  <div class="node node-parties" style="left:680px;top:490px;">
    <svg viewBox="0 0 40 40"><g fill="#000"><polygon points="20,4 23,15 34,15 25,21 28,32 20,25 12,32 15,21 6,15 17,15"/><circle cx="6" cy="6" r="2"/><circle cx="34" cy="6" r="2"/><circle cx="5" cy="34" r="2"/><circle cx="35" cy="34" r="2"/></g></svg>
  </div>
  <div class="node node-puzzles" style="left:460px;top:415px;">
    <svg viewBox="0 0 40 40"><path fill="#000" d="M6 10h9a4 4 0 1 1 8 0h9v9a4 4 0 1 1 0 8v9h-9a4 4 0 1 0-8 0H6v-9a4 4 0 1 0 0-8z"/></svg>
  </div>
  <div class="node node-riddles" style="left:470px;top:515px;">
    <svg viewBox="0 0 40 40"><path fill="#000" d="M6 5h28v24H22l-6 6v-6H6z"/><text x="20" y="24" text-anchor="middle" font-family="Arial, sans-serif" font-weight="700" font-size="18" fill="#fff">?</text></svg>
  </div>
  <div class="node node-mysteries" style="left:570px;top:590px;">
    <svg viewBox="0 0 40 40"><g fill="none" stroke="#000" stroke-width="4"><circle cx="17" cy="17" r="11"/><line x1="25" y1="25" x2="36" y2="36"/></g></svg>
  </div>

  <div class="hub"><span class="hub-name">THE VAULTS<br>of KDW</span></div>

  <span class="label" style="left:868px;top:345px;">Team Building</span>
  <span class="label" style="left:940px;top:433px;">Date Night</span>
  <p class="label-note" style="left:830px;top:455px;width:190px;">THE VAULTS Escape Games are a unique date night activity.</p>
  <span class="label" style="left:985px;top:543px;">Parties</span>
  <p class="label-note" style="left:800px;top:566px;width:260px;">Birthday, anniversary, you name it! For any special events, personalized arrangements can be made and special private group prices are available!</p>
  <span class="label" style="left:290px;top:450px;">Puzzles</span>
  <span class="label" style="left:310px;top:550px;">Riddles</span>
  <span class="label" style="left:360px;top:665px;">Mysteries</span>

</main>
</body>
</html>
```